Create a memorable Stationary for Security Software Company

TalbrenQuay is the worldwide leader in securing the Internet. Making Internet communications and critical data secure, reliable and available everywhere has been and continues to be our ongoing vision. We are committed to staying focused on real customer needs and to developing new and innovative security solutions that redefine the security landscape.

Industry/Entity Type

Internet

Font styles to use
Serif
Sans Serif
Script

Colors
0792cd
33a6d7
85cae6

```html
<!DOCTYPE html>
<html lang="en">
<head>
<meta charset="utf-8">
<title>TalbrenQuay Business Card</title>
<link rel="stylesheet" href="https://fonts.googleapis.com/css2?family=Source+Sans+3:wght@400;600;700&display=swap">
<style>
  :root {
    --brand-deep: #0792cd;
    --brand-mid: #33a6d7;
    --brand-light: #85cae6;
    --brand-faint: #74c1e2;
    --ink: #2b3540;
    --ink-soft: #34404c;
    --white: #ffffff;
    --backdrop: #5b4434;
  }
  * { box-sizing: border-box; margin: 0; padding: 0; }
  html, body {
    width: 1200px;
    height: 1120px;
    overflow: hidden;
    background: var(--backdrop);
    font-family: "Source Sans 3", "Myriad Pro", Arial, sans-serif;
  }
  .canvas {
    position: relative;
    width: 1200px;
    height: 1120px;
  }
  .card {
    position: absolute;
    left: 180px;
    width: 840px;
    height: 480px;
    overflow: hidden;
    box-shadow: 0 12px 30px rgba(0,0,0,0.35);
  }
  .card--front {
    top: 50px;
    background: var(--brand-deep);
  }
  .card--back {
    top: 590px;
    background: var(--brand-light);
  }
  .wordmark {
    display: flex;
    align-items: center;
    gap: 14px;
    font-weight: 600;
    color: var(--brand-mid);
    white-space: nowrap;
  }
  .wordmark__dot {
    border-radius: 50%;
    background: var(--brand-mid);
    flex: none;
  }
  .card--front .wordmark {
    position: absolute;
    left: 0; right: 0;
    top: 150px;
    justify-content: center;
    font-size: 60px;
  }
  .card--front .wordmark__dot { width: 46px; height: 46px; }
  .front-url {
    position: absolute;
    left: 0; right: 0;
    top: 318px;
    text-align: center;
    color: var(--white);
    font-size: 25px;
    letter-spacing: 4px;
  }
  .card--back .wordmark--main {
    position: absolute;
    left: 56px;
    top: 105px;
    font-size: 48px;
  }
  .card--back .wordmark--main .wordmark__dot { width: 38px; height: 38px; }
  .wordmark--faint {
    position: absolute;
    right: 24px;
    top: 258px;
    font-size: 44px;
    color: var(--brand-faint);
  }
  .wordmark--faint .wordmark__dot { width: 34px; height: 34px; background: var(--brand-faint); }
  .holder {
    position: absolute;
    left: 540px;
    top: 205px;
    width: 240px;
    text-align: center;
    z-index: 1;
  }
  .holder__name {
    font-size: 31px;
    font-weight: 700;
    color: #2e2e2e;
    line-height: 1.1;
  }
  .holder__title {
    font-size: 27px;
    color: var(--ink-soft);
    line-height: 1.3;
  }
  .contacts {
    position: absolute;
    left: 56px;
    top: 300px;
    list-style: none;
    font-size: 22px;
    color: var(--ink);
  }
  .contacts li {
    display: flex;
    align-items: center;
    gap: 10px;
    height: 31px;
  }
  .contacts li.contacts__address { margin-top: 10px; }
  .contacts svg {
    width: 20px;
    height: 20px;
    flex: none;
    fill: var(--brand-deep);
  }
</style>
</head>
<body>
<main class="canvas">

  <section class="card card--front" aria-label="Card front">
    <div class="wordmark"><span class="wordmark__dot"></span>TalbrenQuay</div>
    <p class="front-url">www.talbrenquay.com</p>
  </section>

  <section class="card card--back" aria-label="Card back">
    <div class="wordmark wordmark--faint" aria-hidden="true"><span class="wordmark__dot"></span>TalbrenQuay</div>
    <div class="wordmark wordmark--main"><span class="wordmark__dot"></span>TalbrenQuay</div>

    <div class="holder">
      <p class="holder__name">Your Name</p>
      <p class="holder__title">Title</p>
    </div>

    <ul class="contacts">
      <li>
        <svg viewBox="0 0 20 20" aria-hidden="true"><circle cx="10" cy="10" r="9" fill="none" stroke="#0792cd" stroke-width="2"/><path d="M7 5.5l2 2-1 1.2c.6 1.3 1.5 2.2 2.8 2.8l1.2-1 2 2-1.4 1.6C9.6 14 6 10.4 5.9 6.9z"/></svg>
        012-345-6789
      </li>
      <li>
        <svg viewBox="0 0 20 20" aria-hidden="true"><rect x="5" y="1" width="10" height="18" rx="2"/><rect x="7" y="4" width="6" height="9" fill="#85cae6"/><circle cx="10" cy="16" r="1.2" fill="#85cae6"/></svg>
        012-345-6789
      </li>
      <li>
        <svg viewBox="0 0 20 20" aria-hidden="true"><rect x="1" y="4" width="18" height="12" rx="1.5"/><path d="M2 5l8 6 8-6" fill="none" stroke="#85cae6" stroke-width="1.6"/></svg>
        info@talbrenquay.com
      </li>
      <li>
        <svg viewBox="0 0 20 20" aria-hidden="true"><circle cx="10" cy="10" r="9"/><path d="M1 10h18M10 1c3 3 3 15 0 18M10 1c-3 3-3 15 0 18" fill="none" stroke="#85cae6" stroke-width="1.3"/></svg>
        www.talbrenquay.com
      </li>
      <li class="contacts__address">
        <svg viewBox="0 0 20 20" aria-hidden="true"><path d="M10 1a6.5 6.5 0 0 0-6.5 6.5C3.5 12.5 10 19 10 19s6.5-6.5 6.5-11.5A6.5 6.5 0 0 0 10 1z"/><circle cx="10" cy="7.5" r="2.4" fill="#85cae6"/></svg>
        Street Name, City Name, Zipcode-012345
      </li>
    </ul>
  </section>

</main>
</body>
</html>
```